Coffeeshop menu for filter tip

We want to have a cannabis (coffeeshop) menu in the size 25mm wide x 60mm wide. Some examples attached.

it must have the following text:
Menu

WEED p/g
Velotrine €16
Cinderfox €14
Tide Rambler €14
Marigolden €16
Grand Pelican €14
Copper Comet €14

HASH p/g
Baltic Ember €12
Harbor Velvet€11
Plum Rova €14
Dusk Maple €10

Target Market(s)

tourist in Amsterdam

Requirements
Nice to have
• cannabis sign leaf
• No Cigarettes allowed symbol

```html
<!DOCTYPE html>
<html lang="en">
<head>
<meta charset="utf-8">
<title>Amsterdam Menu</title>
<link rel="stylesheet" href="https://fonts.googleapis.com/css2?family=Roboto+Slab:wght@300;700&family=Roboto:wght@400&display=swap">
<style>
  :root {
    --leaf-green: #a6c93f;
    --olive-ink: #4a4a26;
    --board-dark: #2a1c1a;
    --board-mid: #3a2825;
    --paper-white: #ffffff;
    --rule-light: #cfc8c4;
    --rule-olive: #9ea45a;
    --stop-red: #e0322b;
  }
  html, body {
    margin: 0;
    padding: 0;
    width: 1200px;
    height: 2873px;
    overflow: hidden;
    background: var(--board-dark);
  }
  .menu-card {
    display: block;
    width: 1200px;
    height: 2873px;
  }
  .title-small {
    font-family: "Roboto Slab", serif;
    font-weight: 700;
    font-size: 82px;
    fill: var(--paper-white);
    letter-spacing: 1px;
  }
  .title-large {
    font-family: "Roboto Slab", serif;
    font-weight: 700;
    font-size: 206px;
    fill: var(--olive-ink);
  }
  .section-label {
    font-family: "Roboto Slab", serif;
    font-weight: 700;
    font-size: 92px;
    fill: var(--olive-ink);
  }
  .unit-label {
    font-family: "Roboto Slab", serif;
    font-weight: 300;
    font-size: 68px;
    fill: var(--paper-white);
  }
  .item-name, .item-price {
    font-family: "Roboto Slab", serif;
    font-weight: 300;
    font-size: 74px;
    fill: var(--paper-white);
  }
  .name-rule {
    stroke: var(--rule-light);
    stroke-width: 3;
    stroke-dasharray: 3 7;
  }
  .price-rule {
    stroke: var(--rule-olive);
    stroke-width: 3;
    stroke-dasharray: 3 7;
  }
  .ribbon { fill: var(--leaf-green); }
  .footer-note {
    font-family: "Roboto", sans-serif;
    font-weight: 400;
    font-size: 80px;
    fill: var(--paper-white);
  }
</style>
</head>
<body>
<svg class="menu-card" viewBox="0 0 1200 2873" xmlns="http://www.w3.org/2000/svg">
  <defs>
    <linearGradient id="board-grain" x1="0" y1="0" x2="1" y2="1">
      <stop offset="0" stop-color="#2a1c1a"/>
      <stop offset="0.45" stop-color="#3a2825"/>
      <stop offset="1" stop-color="#24181a"/>
    </linearGradient>
  </defs>

  <rect class="board" x="0" y="0" width="1200" height="2873" fill="url(#board-grain)"/>

  <rect class="header-band" x="0" y="0" width="1200" height="484" fill="var(--leaf-green)"/>
  <text class="title-small" x="120" y="205">AMSTERDAM</text>
  <text class="title-large" x="114" y="378">MENU</text>
  <g class="header-emblem" role="img" aria-label="Cannabis leaf emblem in a white ring">
    <circle cx="953" cy="253" r="104" fill="none" stroke="var(--paper-white)" stroke-width="10"/>
    <circle cx="953" cy="253" r="62" fill="var(--olive-ink)" opacity="0.55"/>
  </g>

  <polygon class="ribbon" points="0,652 705,652 750,730 705,808 0,808"/>
  <text class="section-label" x="146" y="762">WEED</text>
  <text class="unit-label" x="889" y="778">p/g</text>

  <g class="price-list weed-list">
    <text class="item-name" x="146" y="990">Velotrine</text>
    <text class="item-price" x="889" y="990">€16</text>
    <line class="name-rule" x1="149" y1="1020" x2="669" y2="1020"/>
    <line class="price-rule" x1="815" y1="1010" x2="1081" y2="1010"/>

    <text class="item-name" x="146" y="1108">Cinderfox</text>
    <text class="item-price" x="889" y="1108">€14</text>
    <line class="name-rule" x1="149" y1="1138" x2="669" y2="1138"/>
    <line class="price-rule" x1="815" y1="1128" x2="1081" y2="1128"/>

    <text class="item-name" x="146" y="1226">Tide Rambler</text>
    <text class="item-price" x="889" y="1226">€14</text>
    <line class="name-rule" x1="149" y1="1256" x2="669" y2="1256"/>
    <line class="price-rule" x1="815" y1="1246" x2="1081" y2="1246"/>

    <text class="item-name" x="146" y="1345">Marigolden</text>
    <text class="item-price" x="889" y="1345">€16</text>
    <line class="name-rule" x1="149" y1="1375" x2="669" y2="1375"/>
    <line class="price-rule" x1="815" y1="1365" x2="1081" y2="1365"/>

    <text class="item-name" x="146" y="1463">Grand Pelican</text>
    <text class="item-price" x="889" y="1463">€14</text>
    <line class="name-rule" x1="149" y1="1493" x2="669" y2="1493"/>
    <line class="price-rule" x1="815" y1="1483" x2="1081" y2="1483"/>

    <text class="item-name" x="146" y="1581">Copper Comet</text>
    <text class="item-price" x="889" y="1581">€14</text>
  </g>

  <polygon class="ribbon" points="0,1765 705,1765 750,1846 705,1927 0,1927"/>
  <text class="section-label" x="146" y="1878">HASH</text>
  <text class="unit-label" x="889" y="1893">p/g</text>

  <g class="price-list hash-list">
    <text class="item-name" x="146" y="2102">Baltic Ember</text>
    <text class="item-price" x="889" y="2102">€12</text>
    <line class="name-rule" x1="149" y1="2132" x2="669" y2="2132"/>
    <line class="price-rule" x1="815" y1="2122" x2="1081" y2="2122"/>

    <text class="item-name" x="146" y="2221">Harbor Velvet</text>
    <text class="item-price" x="889" y="2221">€11</text>
    <line class="name-rule" x1="149" y1="2251" x2="669" y2="2251"/>
    <line class="price-rule" x1="815" y1="2241" x2="1081" y2="2241"/>

    <text class="item-name" x="146" y="2339">Plum Rova</text>
    <text class="item-price" x="889" y="2339">€14</text>
    <line class="name-rule" x1="149" y1="2369" x2="669" y2="2369"/>
    <line class="price-rule" x1="815" y1="2359" x2="1081" y2="2359"/>

    <text class="item-name" x="146" y="2457">Dusk Maple</text>
    <text class="item-price" x="889" y="2457">€10</text>
  </g>

  <g class="no-smoking-icon">
    <circle cx="291" cy="2694" r="72" fill="var(--paper-white)"/>
    <circle cx="291" cy="2694" r="64" fill="none" stroke="var(--stop-red)" stroke-width="16"/>
    <g transform="rotate(-45 291 2694)">
      <rect x="231" y="2682" width="96" height="24" fill="var(--paper-white)" stroke="#bbbbbb" stroke-width="3"/>
      <rect x="327" y="2682" width="22" height="24" fill="#e89a3c"/>
    </g>
    <line x1="246" y1="2649" x2="336" y2="2739" stroke="var(--stop-red)" stroke-width="16"/>
  </g>
  <text class="footer-note" x="453" y="2722">No Cigarette</text>
</svg>
</body>
</html>
```